Medical Practice Business Card

we need a business card for our new medical ophthalmology practice based in Corwin Falls New Hampshire. we are looking for a simple , modern and elegant design.
the card needs to contain the following
1- the logo of our practice (please see attached file)
2- the name of the practice : "Silver Birch Retina Care"
3- Doctor's Name: Tobias Rendell MD PhD
4- Specialty: Board-Certified Vitreoretinal Surgeon
5- practice address: 87 Larkspur Ave, Suite 210, Corwin Falls NH 03481
7- Office number: 617- 482 - 7730
8- fax number: 617- 391 - 2268
9- email: info@sbretinahub.example
10- website: www.sbretinahub.example

```html
<!DOCTYPE html>
<html lang="en">
<head>
<meta charset="utf-8">
<title>Silver Birch Retina Care – Business Card</title>
<link rel="stylesheet" href="https://fonts.googleapis.com/css2?family=Montserrat:wght@400;600;700&display=swap">
<style>
  :root {
    --backdrop: #6b6b6b;
    --navy: #1b3a5f;
    --navy-deep: #14325a;
    --white: #ffffff;
    --ink: #1e1e1e;
    --blue: #1b6fc0;
    --blue-soft: #4aa3d8;
    --cyan: #7fd8ea;
    --icon: #2a79c4;
  }
  * { box-sizing: border-box; margin: 0; padding: 0; }
  html, body {
    width: 1200px; height: 1200px; overflow: hidden;
    background: var(--backdrop);
    font-family: "Montserrat", sans-serif;
  }
  .card {
    position: absolute;
    left: 241px;
    width: 719px;
    height: 420px;
    border-radius: 28px;
    overflow: hidden;
  }
  .card--front { top: 142px; background: var(--navy); }
  .card--back  { top: 638px; background: var(--white); }

  .brand {
    position: absolute;
    display: flex;
    align-items: center;
  }
  .brand__circle {
    flex: none;
    border-radius: 50%;
    border: 3px solid currentColor;
  }
  .brand__name {
    font-weight: 600;
    text-transform: uppercase;
    letter-spacing: 0.02em;
    line-height: 1.25;
    white-space: nowrap;
  }
  .card--front .brand {
    left: 150px; top: 135px;
    gap: 28px;
    color: var(--white);
  }
  .card--front .brand__circle { width: 150px; height: 150px; }
  .card--front .brand__name { font-size: 37px; }

  .card--back .brand {
    right: 40px; top: 38px;
    gap: 16px;
    color: var(--navy-deep);
  }
  .card--back .brand__circle { width: 102px; height: 102px; }
  .card--back .brand__name { font-size: 24px; }

  .doctor {
    position: absolute;
    left: 39px; top: 198px;
  }
  .doctor__name {
    font-size: 31px; font-weight: 700;
    color: var(--blue);
    letter-spacing: 0.01em;
  }
  .doctor__credentials { color: var(--blue-soft); }
  .doctor__role {
    margin-top: 2px;
    font-size: 18.5px; font-weight: 400;
    color: var(--ink);
  }
  .divider {
    position: absolute;
    left: 39px; top: 276px;
    width: 639px; height: 2px;
    background: var(--ink);
  }
  .contacts {
    position: absolute;
    left: 40px; top: 291px;
    list-style: none;
  }
  .contacts li {
    display: flex; align-items: center; gap: 10px;
    height: 27px;
    font-size: 18.5px; color: var(--ink);
  }
  .contacts svg { width: 20px; height: 20px; flex: none; }
  .icon-fill { fill: var(--icon); }
  .icon-line { fill: none; stroke: var(--icon); stroke-width: 2; }
  .address {
    position: absolute;
    right: 42px; top: 333px;
    text-align: right;
    font-size: 18.5px; line-height: 28px;
    color: var(--ink);
    font-style: normal;
  }
  .accent-bar {
    position: absolute;
    left: 0; right: 0; bottom: 0; height: 12px;
    display: flex;
  }
  .accent-bar__navy { width: 480px; background: var(--navy-deep); }
  .accent-bar__cyan { flex: 1; background: var(--cyan); }
</style>
</head>
<body>
  <section class="card card--front" aria-label="Card front">
    <div class="brand">
      <span class="brand__circle"></span>
      <span class="brand__name">Silver Birch<br>Retina Care</span>
    </div>
  </section>

  <section class="card card--back" aria-label="Card back">
    <div class="brand">
      <span class="brand__circle"></span>
      <span class="brand__name">Silver Birch<br>Retina Care</span>
    </div>

    <div class="doctor">
      <h1 class="doctor__name">Tobias Rendell <span class="doctor__credentials">(MD PhD)</span></h1>
      <p class="doctor__role">Board-Certified Vitreoretinal Surgeon</p>
    </div>

    <div class="divider"></div>

    <ul class="contacts">
      <li>
        <svg viewBox="0 0 24 24" aria-hidden="true"><path class="icon-fill" d="M2 10c0-3.5 4.5-6 10-6s10 2.5 10 6v2h-5V9.5H7V12H2z M6 13h12l2 7H4z"/></svg>
        617- 482 - 7730
      </li>
      <li>
        <svg viewBox="0 0 24 24" aria-hidden="true"><path class="icon-fill" d="M7 3h10v5H7z M3 9h18v11H3z"/><path d="M6 12h3v2H6z M11 12h3v2h-3z M6 16h3v2H6z M11 16h3v2h-3z" fill="#fff"/></svg>
        617- 391 - 2268
      </li>
      <li>
        <svg viewBox="0 0 24 24" aria-hidden="true"><path class="icon-fill" d="M2 6h20v12H2z"/><path d="M3 7l9 6 9-6" fill="none" stroke="#fff" stroke-width="1.6"/></svg>
        info@sbretinahub.example
      </li>
      <li>
        <svg viewBox="0 0 24 24" aria-hidden="true"><circle class="icon-line" cx="12" cy="12" r="9"/><ellipse class="icon-line" cx="12" cy="12" rx="4" ry="9"/><path class="icon-line" d="M3 12h18 M5 7h14 M5 17h14"/></svg>
        www.sbretinahub.example
      </li>
    </ul>

    <address class="address">87 Larkspur Ave, Suite 210,<br>Corwin Falls NH 03481</address>

    <div class="accent-bar">
      <span class="accent-bar__navy"></span>
      <span class="accent-bar__cyan"></span>
    </div>
  </section>
</body>
</html>
```